Sponsor at Title Insurance Industry Seminar for Continuing Ed - 250 Companies in Attendance

I offer escrow accounting services in the Title Insurance Industry. I've attached logo files and an example of my former company. I don't like the design and it's a little wordy but it provides detail of what I offer.

Below is a brief write-up...
For professionals in the title insurance industry, finding a reliable and cost-effective solution to escrow accounting needs can feel overwhelming. When choosing the right accounting partner, title companies and law firms need a group they can trust, and that’s where we come in. Brightfern Ledger Solutions is a team that understands the title industry and the importance of compliance, security and accuracy. Brightfern Ledger Solutions is the experienced, convenient and cost-effective choice for the accounting and certification needs of companies throughout the country.

```html
<!DOCTYPE html>
<html lang="en">
<head>
<meta charset="utf-8">
<title>Brightfern Ledger Solutions – Escrow Reconciliation Flyer</title>
<link rel="stylesheet" href="https://fonts.googleapis.com/css2?family=Fira+Sans:wght@600;700&family=Hind:wght@400;500&display=swap">
<style>
:root{
  --copper:#bd7662;
  --navy:#353f4f;
  --ink:#3b4250;
  --paper:#ffffff;
  --backdrop:#e6e6e9;
  --photo-dark:#2c3544;
  --photo-warm:#c98a70;
}
*{box-sizing:border-box;margin:0;padding:0}
html,body{width:955px;height:1200px;overflow:hidden;background:var(--backdrop)}
.flyer{position:absolute;left:75px;top:79px;width:804px;height:1040px;background:var(--paper);overflow:hidden;font-family:"Hind",sans-serif;color:var(--ink)}
.abs{position:absolute}
.brand{left:64px;top:112px;display:flex;align-items:center;gap:12px}
.brand-dot{width:30px;height:30px;border-radius:50%;background:var(--copper)}
.brand-name{font-family:"Fira Sans",sans-serif;font-weight:700;font-size:28px;line-height:30px;color:var(--navy)}
.hero-band{left:0;top:272px}
.hero-photo{left:0;top:0}
.headline{left:48px;top:314px;font-family:"Fira Sans",sans-serif;font-weight:700;font-size:30px;line-height:39px;color:#fff;letter-spacing:.2px}
.section-title{font-family:"Fira Sans",sans-serif;font-weight:700}
.experience{left:48px;top:492px;font-size:31px;color:var(--navy)}
.perks{left:52px;top:536px;list-style:none;font-size:17px;line-height:27px}
.perks li{padding-left:19px;position:relative}
.perks li::before{content:"";position:absolute;left:0;top:10px;width:7px;height:7px;border:1.5px solid var(--copper);border-radius:50%}
.about-title{left:46px;top:608px;font-size:31px;color:var(--copper)}
.about-copy{left:46px;top:648px;width:355px;font-size:16.5px;line-height:23.2px}
.about-copy p+p{margin-top:10px}
.call-label{left:54px;top:851px;width:252px;text-align:center;font-family:"Fira Sans",sans-serif;font-weight:700;font-size:21px;color:var(--navy)}
.call-button{left:54px;top:881px;width:252px;height:53px;border:2px solid var(--navy);border-radius:27px;padding:3px}
.call-button span{display:flex;align-items:center;justify-content:center;width:100%;height:100%;background:var(--copper);border-radius:23px;color:#fff;font-family:"Fira Sans",sans-serif;font-weight:700;font-size:20px}
.contact{left:47px;display:flex;align-items:center;gap:7px;font-size:16px}
.contact-icon{width:26px;height:26px;border-radius:50%;background:var(--copper);display:flex;align-items:center;justify-content:center}
.feature{width:150px;text-align:center;font-size:16px}
.feature svg{display:block;margin:0 auto 6px}
.services{left:420px;top:719px;width:332px;height:204px;background:var(--copper);border-radius:40px 0 55px 0}
.services-tab{left:415px;top:733px;width:246px;height:48px;background:var(--navy);border-radius:0 8px 8px 0;color:#fff;font-family:"Fira Sans",sans-serif;font-weight:700;font-size:28px;line-height:48px;padding-left:32px}
.services-list{left:446px;top:799px;list-style:none;color:#fff;font-family:"Fira Sans",sans-serif;font-weight:700;font-size:17.5px;line-height:35px}
.services-list li{padding-left:14px;position:relative}
.services-list li::before{content:"";position:absolute;left:0;top:15px;width:6px;height:6px;background:#fff;border-radius:50%}
.badge{width:100px;height:70px;text-align:center}
.badge-disc{position:absolute;left:17px;top:0;width:66px;height:66px;border-radius:50%;background:var(--navy)}
.badge-pct{position:absolute;left:0;right:0;top:8px;font-family:"Fira Sans",sans-serif;font-weight:700;font-size:16px;color:#e0a48f}
.badge-label{position:absolute;left:-5px;right:-5px;top:30px;background:#fff;font-size:17px;line-height:20px;color:var(--navy)}
.base-band{left:0;top:1030px;width:804px;height:10px;background:linear-gradient(90deg,var(--copper) 0 399px,var(--navy) 399px)}
</style>
</head>
<body>
<main class="flyer">
  <div class="abs brand"><span class="brand-dot"></span><div class="brand-name">Brightfern<br>Ledger Solutions</div></div>

  <svg class="abs hero-photo" width="804" height="470" viewBox="0 0 804 470">
    <polygon points="0,308 36,272 480,272 480,470 36,470 0,434" fill="var(--copper)"/>
    <polygon points="553,0 804,0 804,470 620,470" fill="var(--copper)"/>
    <defs>
      <linearGradient id="photoTone" x1="0" y1="0" x2="1" y2="1">
        <stop offset="0" stop-color="var(--photo-warm)"/>
        <stop offset=".5" stop-color="#8a6a63"/>
        <stop offset="1" stop-color="var(--photo-dark)"/>
      </linearGradient>
    </defs>
    <path role="img" aria-label="Photo of two smiling business colleagues reviewing a tablet together" d="M440,120 Q520,100 600,110 Q680,100 760,130 L804,170 L804,470 L297,470 Q330,420 400,400 Q430,340 470,310 Q440,240 440,120 Z" fill="url(#photoTone)"/>
  </svg>

  <h1 class="abs headline">PROFESSIONAL ESCROW<br>RECONCILIATION<br>SERVICES</h1>

  <h2 class="abs section-title experience">Experiences Way</h2>
  <ul class="abs perks">
    <li>Secure in Escrow Accounting</li>
    <li>Expert Accounting Team</li>
  </ul>

  <h2 class="abs section-title about-title">About Us</h2>
  <div class="abs about-copy">
    <p>Lorem Ipsum is simply dummy text of the printing and typesetting industry. Lorem Ipsum has been the industry's standard dummy text ever since the 1500s, when an unknown printer took a galley of type and scrambled it to make a type book.</p>
    <p>Lorem Ipsum is simply dummy text of the printing and typesetting industry industry's standard.</p>
  </div>

  <div class="abs call-label">Call Today</div>
  <div class="abs call-button"><span>0909 0047 815</span></div>

  <div class="abs contact" style="top:958px">
    <span class="contact-icon"><svg width="14" height="14" viewBox="0 0 14 14" fill="none" stroke="#fff" stroke-width="1.2"><circle cx="7" cy="7" r="6"/><ellipse cx="7" cy="7" rx="2.6" ry="6"/><line x1="1" y1="7" x2="13" y2="7"/></svg></span>
    brightfernledger.com
  </div>
  <div class="abs contact" style="top:994px">
    <span class="contact-icon"><svg width="14" height="12" viewBox="0 0 14 12" fill="none" stroke="#fff" stroke-width="1.2"><rect x="1" y="1" width="12" height="10"/><polyline points="1,1 7,6.5 13,1"/></svg></span>
    mail@brightfernledger.com
  </div>

  <div class="abs feature" style="left:434px;top:499px">
    <svg width="60" height="60" viewBox="0 0 60 60" fill="none" stroke="var(--copper)" stroke-width="1.4"><circle cx="30" cy="30" r="28" stroke-width="3"/><rect x="18" y="16" width="20" height="26" rx="1"/><line x1="22" y1="34" x2="32" y2="34"/><line x1="22" y1="38" x2="30" y2="38"/><path d="M22,25 l4,-4 4,3 4,-4"/><circle cx="40" cy="40" r="5"/></svg>
    2 Way Reconciliation
  </div>
  <div class="abs feature" style="left:597px;top:499px">
    <svg width="60" height="60" viewBox="0 0 60 60" fill="none" stroke="var(--copper)" stroke-width="1.4"><circle cx="30" cy="30" r="28" stroke-width="3"/><rect x="17" y="18" width="26" height="20" rx="2"/><line x1="17" y1="23" x2="43" y2="23"/><path d="M24,29 l-3,2 3,2 M30,28 l-2,6 M34,29 l3,2 -3,2"/><circle cx="41" cy="38" r="5"/></svg>
    Software System
  </div>
  <div class="abs feature" style="left:434px;top:609px">
    <svg width="60" height="60" viewBox="0 0 60 60" fill="none" stroke="var(--copper)" stroke-width="1.4"><circle cx="30" cy="30" r="28" stroke-width="3"/><rect x="22" y="17" width="20" height="11" rx="1"/><circle cx="32" cy="22.5" r="3"/><path d="M14,35 h8 l6,3 h8 l7,-5 M14,40 h6 l8,3 h6"/></svg>
    Affordable Price
  </div>
  <div class="abs feature" style="left:597px;top:609px">
    <svg width="60" height="60" viewBox="0 0 60 60" fill="none" stroke="var(--copper)" stroke-width="1.4"><circle cx="30" cy="30" r="28" stroke-width="3"/><rect x="20" y="15" width="20" height="30" rx="1"/><path d="M23,21 l1.5,1.5 3,-3 M23,28 l1.5,1.5 3,-3 M23,35 l1.5,1.5 3,-3"/><line x1="29" y1="21" x2="37" y2="21"/><line x1="29" y1="28" x2="37" y2="28"/><line x1="29" y1="35" x2="37" y2="35"/><rect x="23" y="39" width="3" height="3"/></svg>
    Daily Reports
  </div>

  <div class="abs services"></div>
  <div class="abs services-tab">Our Services</div>
  <ul class="abs services-list">
    <li>Escrow Reconciliation Services</li>
    <li>TLPA Best Practice Certification</li>
    <li>Other Related Services</li>
  </ul>

  <div class="abs badge" style="left:407px;top:943px"><span class="badge-disc"></span><span class="badge-pct">100%</span><span class="badge-label">Compliance</span></div>
  <div class="abs badge" style="left:539px;top:943px"><span class="badge-disc"></span><span class="badge-pct">100%</span><span class="badge-label">Convenience</span></div>
  <div class="abs badge" style="left:665px;top:943px"><span class="badge-disc"></span><span class="badge-pct">100%</span><span class="badge-label">Credibility</span></div>

  <div class="abs base-band"></div>
</main>
</body>
</html>
```